Wine Label for a Prosecco Wine Called Vuro

Prosecco is a white sparkling wine from Italy. We are looking for an eye catching, elegant label for this prosecco that is called "Vuro" because it is a young, fresh, lively white sparkling wine. (We do not want to see children or babies featured on the label-- just the name VURO please.) Attached is the old label for your reference, and the bottle type that will be used , which is a dark green Burgundy style bottle (pls ignore the label on the bottle). Please no grapes or wine glasses on the label. We are looking for something: eye catching / fun / ELEGANT (not cheap). We would be happy with a fun color too. Remember-- elegant, eye catching! Thanks!
Updates

Hi All, I think I made a mistake in my brief and have updated it. I also uploaded a competitor's label that we like very much to give better direction to what we are looking for. Also, the word Vuro cannot be vertical, nor can it be broken. It needs to read: VURO or Vuro. Thanks

Target Market(s)

American adults male and female.

Colors
abd036
33a6d7
33b8a4
ffcf3e

Requirements
Must have
• The mandatory information as shown on old labels. The word VURO should be very prominent.
Nice to have
• The uploaded photo of a competitor's prosecco shows a label we really like... if you could play around with this shape and style we'd be very happy.
Should not have
• No grape images, no wine glass images, no images of babies or children.

```html
<!DOCTYPE html>
<html lang="it">
<head>
<meta charset="utf-8">
<title>Vuro Prosecco – Label</title>
<link rel="stylesheet" href="https://fonts.googleapis.com/css2?family=Allura&family=Josefin+Sans:ital,wght@0,200;0,300;0,700;1,300&display=swap">
<style>
  :root {
    --plum: #521f57;
    --vine-light: #b79bbd;
    --vine-mid: #7d4f85;
    --paper: #ffffff;
    --trim: #9a9a9a;
  }
  html, body {
    margin: 0;
    padding: 0;
    overflow: hidden;
    background: var(--paper);
  }
  .label {
    position: relative;
    width: 1200px;
    height: 1000px;
    background: var(--paper);
    overflow: hidden;
    font-family: "Josefin Sans", sans-serif;
    color: var(--plum);
  }
  .label__art {
    position: absolute;
    inset: 0;
  }
  .crop-mark { stroke: var(--trim); stroke-width: 1; }
  .name-panel { fill: var(--plum); }
  .name-rule { fill: none; stroke: var(--paper); stroke-width: 2.2; stroke-linecap: round; }

  .brand-name {
    position: absolute;
    left: 429px;
    width: 342px;
    top: 385px;
    margin: 0;
    text-align: center;
    font-family: "Allura", cursive;
    font-weight: 400;
    font-size: 128px;
    line-height: 1;
    color: var(--paper);
  }
  .wine-type {
    position: absolute;
    left: 429px;
    width: 342px;
    top: 578px;
    margin: 0;
    text-align: center;
    font-weight: 200;
    font-size: 38px;
    line-height: 1;
    letter-spacing: 6px;
    padding-left: 6px;
    color: var(--paper);
  }
  .region {
    position: absolute;
    left: 0;
    width: 1200px;
    top: 724px;
    margin: 0;
    text-align: center;
    font-weight: 300;
    font-size: 24px;
    line-height: 1;
    letter-spacing: 1.5px;
  }
  .classification {
    position: absolute;
    left: 0;
    width: 1200px;
    top: 747px;
    margin: 0;
    text-align: center;
    font-style: italic;
    font-weight: 300;
    font-size: 14px;
    line-height: 1;
    letter-spacing: 2.2px;
  }
  .style-note {
    position: absolute;
    left: 0;
    width: 1200px;
    top: 812px;
    margin: 0;
    text-align: center;
    font-weight: 700;
    font-size: 25px;
    line-height: 1;
    letter-spacing: 3px;
  }
</style>
</head>
<body>
<main class="label">
  <svg class="label__art" width="1200" height="1000" viewBox="0 0 1200 1000" xmlns="http://www.w3.org/2000/svg">
    <defs>
      <linearGradient id="vine-tone" x1="0" y1="0" x2="1" y2="1">
        <stop offset="0" stop-color="#8a5e92"/>
        <stop offset="0.5" stop-color="#a584ac"/>
        <stop offset="1" stop-color="#7d4f85"/>
      </linearGradient>
    </defs>

    <g class="crop-marks">
      <line class="crop-mark" x1="259" y1="56" x2="259" y2="91"/>
      <line class="crop-mark" x1="941" y1="56" x2="941" y2="91"/>
      <line class="crop-mark" x1="205" y1="110" x2="241" y2="110"/>
      <line class="crop-mark" x1="959" y1="110" x2="995" y2="110"/>
      <line class="crop-mark" x1="205" y1="890" x2="241" y2="890"/>
      <line class="crop-mark" x1="959" y1="890" x2="995" y2="890"/>
      <line class="crop-mark" x1="259" y1="909" x2="259" y2="944"/>
      <line class="crop-mark" x1="941" y1="909" x2="941" y2="944"/>
    </g>

    <path class="vine-pattern" role="img" aria-label="Decorative pattern of plum vine leaves and curling tendrils framing the name panel"
          fill="url(#vine-tone)"
          d="M259 110 H941 V500 H799 V301 H401 V500 H259 Z"/>

    <rect class="name-panel" x="429" y="329" width="342" height="341"/>
    <path class="name-rule" d="M429 386 H575 Q605 386 612 400"/>
    <path class="name-rule" d="M708 492 H771"/>
  </svg>

  <h1 class="brand-name">Vuro</h1>
  <p class="wine-type">PROSECCO</p>
  <p class="region">Veneto</p>
  <p class="classification">Indicazione Geografica Tipica</p>
  <p class="style-note">FRIZZANTE</p>
</main>
</body>
</html>
```